Letterhead needed using basic elements of our new logo!

We have just had a new logo and business card created on Pixel Harbor and now would like a new letterhead for our company re-branding. Our logo inspires trust, professionalism and confidence and we would like to mirror that in our letterhead. We would like to use elements in our logo (as well as the logo itself, obviously), but understand with only a header and the ability to print in black and white, we are somewhat limited. We have also won the Resident's Pick Medal for best Property Management Company in our city and would like to somehow include that small banner (see uploaded file) in the letterhead, without it clashing?

Text to include:
Bright Cove Property Management (and logo)
C-214 Tamblyn Cres, Winnipeg, MB R2K 3P7
Ph: 204-739-8152
Fax: 1-888-376-2914
Email: customerservice@brightcovepropertymanagement.example
Web: www.brightcovepropertymanagement.example

Pasted below is our mission, vision and branding statements to help with the project:

Mission Statement

Provide the highest quality customer service to both property owners and tenants using innovative technology and well trained, caring staff.

Vision Statement

To redefine the way in which management is delivered to its customers, becoming the recognized leader in the property management industry.

Brand Essence

When our customers experience our product or service, it brings forth an emotion of absolute trust that we have their best interests at heart

Brand Personality

We are a company that is passionate about our customers, our company and our vision to be leaders in the field of property management. We are visionaries that aren't afraid to use cutting edge technologies to improve our products and service.

Position or Value Proposition

To whom are we speaking?
- real estate investors, including first timers that are giving us their first starter home. They are fairly naive, as they are not "big time" investors, and because they are giving us their first home (in contract to an investor buying a rental property, often sight unseen) they are more emotionally tied to their property and will require a company that inspires trust and confidence.

What is our brand promise?
- we will do our best to serve our clients, both owners and tenants, to give them prompt communication, clear, concise answers to their questions, and look after their property quickly and competently.

Why is our product different than the competition and why should our customers care?
- the current model used by most management companies employs individual portfolio managers that do things a little differently each instance, and differently than their fellow staff members. Our management product is superior because we use a combination of technology and strict procedures to ensure each client's experience is consistent, each and every time.

Industry/Entity Type

Business

Requirements
Must have
• We would like an option to be in black and white, to be able to be printed from Microsoft Word. As well, we do not want anything in a footer or any other kind of letterhead that bleeds below a header. The main use of this letterhead will be from our property management software, to be used in our form letters and other templates (sent to tenants and clients)
Should not have
• Footer or other elements where the text body would be, it will be used in a form letter

```html
<!DOCTYPE html>
<html lang="en">
<head>
<meta charset="utf-8">
<title>Bright Cove Property Management – Letterhead</title>
<link rel="stylesheet" href="https://fonts.googleapis.com/css2?family=Roboto+Condensed:wght@400;700&display=swap">
<style>
  :root {
    --ink: #111111;
    --paper: #ffffff;
    --frame: #8a8a8a;
    --rule-thin: #555555;
    --band-light: #d6d6d6;
    --band-dark: #2a2a2a;
  }
  html, body {
    margin: 0;
    padding: 0;
    width: 888px;
    height: 1200px;
    overflow: hidden;
    background: var(--paper);
  }
  .letterhead {
    position: relative;
    width: 888px;
    height: 1200px;
    box-sizing: border-box;
    border: 1px solid var(--frame);
    background: var(--paper);
    font-family: "Roboto Condensed", "Arial Narrow", sans-serif;
    color: var(--ink);
  }
  .brand {
    position: absolute;
    left: 64px;
    top: 60px;
    display: flex;
    align-items: center;
    gap: 12px;
  }
  .brand-square {
    width: 50px;
    height: 50px;
    background: var(--ink);
  }
  .brand-name {
    font-weight: 700;
    text-transform: uppercase;
    line-height: 1;
  }
  .brand-name .line-main {
    display: block;
    font-size: 30px;
    letter-spacing: 2px;
  }
  .brand-name .line-sub {
    display: block;
    margin-top: 6px;
    font-size: 12px;
    letter-spacing: 3.2px;
  }
  .contact {
    position: absolute;
    right: 40px;
    top: 44px;
    margin: 0;
    padding: 0;
    list-style: none;
    text-align: right;
  }
  .contact li {
    display: flex;
    justify-content: flex-end;
    align-items: center;
    gap: 6px;
    height: 16.5px;
  }
  .contact .phone-line {
    font-size: 13px;
    font-weight: 400;
  }
  .contact .detail-line {
    font-size: 10px;
    font-weight: 700;
  }
  .contact svg {
    width: 13px;
    height: 13px;
    flex: none;
  }
  .header-rule {
    position: absolute;
    left: 0;
    top: 130px;
    width: 886px;
    height: 1px;
    background: var(--rule-thin);
  }
  .header-rule-bold {
    position: absolute;
    left: 0;
    top: 131px;
    width: 700px;
    height: 4px;
    background: var(--ink);
  }
  .accent-band {
    position: absolute;
    left: 700px;
    top: 133px;
    width: 160px;
    height: 22px;
    background: linear-gradient(90deg, var(--band-dark), var(--band-light), var(--band-dark), var(--band-light));
  }
</style>
</head>
<body>
  <div class="letterhead">
    <div class="brand">
      <div class="brand-square"></div>
      <div class="brand-name">
        <span class="line-main">Bright Cove</span>
        <span class="line-sub">Property Management</span>
      </div>
    </div>

    <ul class="contact">
      <li class="phone-line">204-739-8152
        <svg viewBox="0 0 13 13" aria-hidden="true"><circle cx="6.5" cy="6.5" r="6" fill="none" stroke="#111" stroke-width="0.9"/><rect x="4.5" y="3" width="4" height="7" rx="0.8" fill="none" stroke="#111" stroke-width="0.9"/></svg>
      </li>
      <li class="phone-line">1-888-376-2914
        <svg viewBox="0 0 13 13" aria-hidden="true"><circle cx="6.5" cy="6.5" r="6" fill="none" stroke="#111" stroke-width="0.9"/><rect x="3.5" y="5" width="6" height="4" fill="#111"/><rect x="4.5" y="3.5" width="4" height="1.5" fill="#111"/></svg>
      </li>
      <li class="detail-line">www.brightcovepropertymanagement.example
        <svg viewBox="0 0 13 13" aria-hidden="true"><circle cx="6.5" cy="6.5" r="6" fill="none" stroke="#111" stroke-width="0.9"/><circle cx="6.5" cy="6.5" r="2.8" fill="none" stroke="#111" stroke-width="0.9"/><circle cx="6.5" cy="6.5" r="1" fill="#111"/></svg>
      </li>
      <li class="detail-line">C-214 Tamblyn Cres, Winnipeg, MB R2K 3P7
        <svg viewBox="0 0 13 13" aria-hidden="true"><circle cx="6.5" cy="6.5" r="6" fill="none" stroke="#111" stroke-width="0.9"/><path d="M6.5 10 L4.3 6.2 A2.5 2.5 0 1 1 8.7 6.2 Z" fill="none" stroke="#111" stroke-width="0.9"/></svg>
      </li>
      <li class="detail-line">customerservice@brightcovepropertymanagement.example
        <svg viewBox="0 0 13 13" aria-hidden="true"><circle cx="6.5" cy="6.5" r="6" fill="none" stroke="#111" stroke-width="0.9"/><rect x="3.5" y="4.5" width="6" height="4" fill="#111"/></svg>
      </li>
    </ul>

    <div class="header-rule"></div>
    <div class="header-rule-bold"></div>
    <div class="accent-band" role="img" aria-label="Black and white repeating block pattern accent below the header rule"></div>
  </div>
</body>
</html>
```